Brand design for Corvanel Holdings

We are a new start up Fund Manager based in Singapore in need of a stylish and slick corporate identity starting with letterhead and business card (2 separate projects on pixel bazaar but must be completed as one). We are aiming to be a somewhat 'budget' service provider with a target market of high net worth individuals and savvy self traders so we need to have our look convey value but with style. Our logo is attached and the use of the blue is imperative. The company name is Corvanel Holdings Pte Ltd and the verbiage 'Licensed by the Treasury Conduct Bureau of Singapore - QTLD licence no. XQZ908172-3' should be incorporated in small print.

Business card should also include address, office, direct and mobile numbers as well as email address. Follow me on blabber/pk/workloop/Zentro+ should also be incrorporated. We are also looking to have a QR code on the business card that people can read with a smartphone which will auto populate our contact details in to their address book.

Many thanks and happy designing!

Reason: Extending so we can have further internal discussions. Thanks for input so far, some great designs coming through! Cheers

```html
<!DOCTYPE html>
<html lang="en">
<head>
<meta charset="utf-8">
<title>Corvanel Holdings Letterhead</title>
<link href="https://fonts.googleapis.com/css2?family=Open+Sans:wght@400;600&display=swap" rel="stylesheet">
<style>
  :root {
    --brand-blue: #0d4ea2;
    --paper: #ffffff;
    --on-blue: #ffffff;
  }
  * { margin: 0; padding: 0; box-sizing: border-box; }
  html, body {
    width: 1009px;
    height: 1200px;
    overflow: hidden;
    background: var(--paper);
  }
  .letterhead {
    position: relative;
    width: 1009px;
    height: 1200px;
    background: var(--paper);
    font-family: "Open Sans", sans-serif;
    color: var(--brand-blue);
  }
  .brand-name {
    position: absolute;
    left: 44px;
    top: 74px;
    font-size: 54px;
    font-weight: 600;
    letter-spacing: 0.5px;
    line-height: 1;
    color: var(--brand-blue);
  }
  .company-block {
    position: absolute;
    left: 680px;
    top: 16px;
    right: 0;
  }
  .company-name {
    font-size: 23px;
    font-weight: 400;
    line-height: 30px;
    white-space: nowrap;
  }
  .company-address {
    font-style: normal;
    font-size: 18px;
    line-height: 20px;
  }
  .web-bar {
    position: absolute;
    left: 680px;
    right: 3px;
    top: 107px;
    height: 20px;
    background: var(--brand-blue);
    color: var(--on-blue);
    font-size: 16px;
    line-height: 20px;
    padding-left: 5px;
  }
  .licence-note {
    position: absolute;
    left: 0;
    right: 0;
    bottom: 10px;
    text-align: center;
    font-size: 16px;
    line-height: 20px;
  }
</style>
</head>
<body>
  <main class="letterhead">
    <div class="brand-name">CORVANEL.COM</div>

    <div class="company-block">
      <div class="company-name">Corvanel Holdings Pte Ltd</div>
      <address class="company-address">
        14 Arden Quay Rd<br>
        Singapore 238512<br>
        P: +65 0000 4812
      </address>
    </div>
    <div class="web-bar">www.corvanel.com</div>

    <p class="licence-note">Licensed by the Treasury Conduct Bureau of Singapore - QTLD licence no. XQZ908172-3</p>
  </main>
</body>
</html>
```